Coastal Bright Sweep Business Card

We are a cleaning and waste management company with the slogan "making waste to landfill a thing of the past". We would like a re-design of our current business card. On the front we want to continue to use our logo as the focus point. On the back, we want the whole thing re-done to be less busy. We want the staff member’s name, the job title, mobile number, email and website. We do not want the address on the card. We still want the green, black and blue colours used, but a new font for the information on the back. Please do not change the logo design at all. We are also thinking about using icons to replace the text ‘mobile, email, website’. The “events + commercial” banner needs to be incorporated somewhere and needs to read “events + commercial + waste”. Another important point for consideration is that we are very concerned about being environmentally sustainable and will be printing on recycled paper. All designs should be made to compliment this in regards to boldness and colouring. Please find attached our logo, our colour chart and an image of our current business card.

```html
<!DOCTYPE html>
<html lang="en">
<head>
<meta charset="utf-8">
<title>Coastal Bright Sweep Business Card</title>
<link href="https://fonts.googleapis.com/css2?family=Lato:wght@400;700&family=Roboto:wght@700;900&display=swap" rel="stylesheet">
<style>
  :root {
    --stage: #000000;
    --paper: #ffffff;
    --navy: #10426f;
    --ink: #123a66;
    --green: #7dc242;
    --blue: #1ba9e1;
    --rule: #a9d8ef;
    --plus: #9aa7b6;
  }
  html, body {
    margin: 0;
    padding: 0;
    width: 1200px;
    height: 900px;
    overflow: hidden;
    background: var(--stage);
  }
  .stage {
    position: relative;
    width: 1200px;
    height: 900px;
  }
  .card {
    position: absolute;
    top: 275px;
    width: 477px;
    height: 293px;
    box-sizing: border-box;
  }
  .card--contact {
    left: 116px;
    background: var(--paper);
    border-radius: 0 48px 0 48px;
  }
  .card--brand {
    left: 622px;
    top: 276px;
    height: 292px;
    background: var(--navy);
    border-radius: 48px 0 48px 0;
  }

  .wordmark {
    font-family: "Roboto", Arial, sans-serif;
    font-weight: 700;
    line-height: 1;
    margin: 0;
  }
  .wordmark span { display: block; }
  .wordmark .wm-top { font-size: 17px; letter-spacing: 2px; }
  .wordmark .wm-big { font-size: 38px; letter-spacing: -0.5px; }

  .card--contact .wordmark {
    position: absolute;
    right: 33px;
    top: 60px;
    text-align: right;
    color: var(--ink);
  }
  .card--brand .wordmark {
    position: absolute;
    left: 0;
    right: 0;
    top: 77px;
    text-align: center;
    color: var(--paper);
  }

  .person {
    position: absolute;
    left: 26px;
    top: 174px;
    width: 426px;
  }
  .person__name {
    margin: 0;
    font-family: "Roboto", Arial, sans-serif;
    font-weight: 700;
    font-size: 18px;
    letter-spacing: 0.2px;
    line-height: 20px;
  }
  .person__first { color: var(--green); }
  .person__last { color: var(--blue); }
  .person__role {
    display: flex;
    align-items: center;
    gap: 6px;
    margin: 0;
    font-family: "Lato", Arial, sans-serif;
    font-size: 13px;
    color: var(--ink);
    line-height: 17px;
  }
  .person__role::after {
    content: "";
    flex: 1;
    height: 1px;
    background: var(--rule);
  }

  .contact-list {
    position: absolute;
    left: 26px;
    top: 218px;
    margin: 0;
    padding: 0;
    list-style: none;
    font-family: "Lato", Arial, sans-serif;
    font-size: 13.5px;
    color: var(--ink);
  }
  .contact-list li {
    display: flex;
    align-items: center;
    gap: 3px;
    height: 17.5px;
  }
  .contact-list svg { width: 11px; height: 11px; flex: none; }

  .divider {
    position: absolute;
    left: 87px;
    width: 303px;
    top: 209px;
    height: 1px;
    background: #4b7aa6;
  }
  .services {
    position: absolute;
    left: 0;
    right: 0;
    top: 231px;
    margin: 0;
    text-align: center;
    font-family: "Roboto", Arial, sans-serif;
    font-weight: 700;
    font-size: 17.5px;
    letter-spacing: 0.2px;
  }
  .services .svc-events { color: var(--paper); }
  .services .svc-commercial { color: var(--green); }
  .services .svc-waste { color: var(--blue); }
  .services .svc-plus { color: var(--plus); font-size: 14px; margin: 0 4px; }
</style>
</head>
<body>
<main class="stage">

  <section class="card card--contact" aria-label="Business card, contact side">
    <h1 class="wordmark">
      <span class="wm-top">COASTAL</span>
      <span class="wm-big">Bright</span>
      <span class="wm-big">Sweep</span>
    </h1>

    <div class="person">
      <p class="person__name"><span class="person__first">MORGAN</span> <span class="person__last">ELLERY</span></p>
      <p class="person__role">Client Manager</p>
    </div>

    <ul class="contact-list">
      <li>
        <svg viewBox="0 0 12 12" aria-hidden="true"><path fill="#123a66" d="M1 4.2C1 2.6 3.2 1.5 6 1.5s5 1.1 5 2.7v.9H8.6V3.9H3.4v1.2H1zM2.5 6h7l1 4.5h-9zM6 6.8a1.5 1.5 0 1 0 0 3 1.5 1.5 0 0 0 0-3z"/></svg>
        0400 555 218
      </li>
      <li>
        <svg viewBox="0 0 12 12" aria-hidden="true"><rect x="1" y="2.5" width="10" height="7" fill="#7dc242"/><path d="M1.3 2.9 6 6.6l4.7-3.7" fill="none" stroke="#ffffff" stroke-width="1"/></svg>
        mellery@coastalbrightsweep.com.au
      </li>
      <li>
        <svg viewBox="0 0 12 12" aria-hidden="true"><circle cx="6" cy="6" r="5" fill="#1ba9e1"/><path d="M3.5 3.5c1 .5 1.5 1.3 1.2 2.3-.3.8.5 1.3 1 1.8.4.5.2 1.5-.2 2.2M7.5 2c-.2.8.3 1.3 1 1.6.8.3 1.5 1 1.4 2" fill="none" stroke="#ffffff" stroke-width="0.9"/></svg>
        www.coastalbrightsweep.com.au
      </li>
    </ul>
  </section>

  <section class="card card--brand" aria-label="Business card, brand side">
    <h2 class="wordmark">
      <span class="wm-top">COASTAL</span>
      <span class="wm-big">Bright</span>
      <span class="wm-big">Sweep</span>
    </h2>
    <div class="divider"></div>
    <p class="services">
      <span class="svc-events">EVENTS</span><span class="svc-plus">+</span><span class="svc-commercial">COMMERCIAL</span><span class="svc-plus">+</span><span class="svc-waste">WASTE</span>
    </p>
  </section>

</main>
</body>
</html>
```